K9 Orbit needs a business card designed

We need a business card designed for K9 Orbit, an expansion of K9 Technics Pty Ltd (www.k9orbit.com.au)

We provide high quality professional services for the Australian space industry. Our clients include the Southern Stellar Bureau and companies working in the space industry. We identify people with space related skills both locally and internationally who are then contracted by clients to create products and support space launch activities.

Colours to be used:
- Navy blue #000080
- Rocket metallic #8A7F8D
- Platinum #E5E4E2
- Black #000000
- White #FFFFFF

*Front of the card*
I have attached our K9 Orbit logo, which needs to be the main item on the card. The 'Space' text should be placed to the right of the 'K9' part rather than below, similar to the attached K9 Orbit card, which this card should match.

If subtext is included, however, it should read ‘Labour Hire • Consultancy • Project Delivery’ rather than the ‘Labour Hire • Consultancy • Project Delivery’ of the K9 Orbit card.

A black background (rather than blue background in the K9 Orbit card) might be good, with a white pattern as in the K9 Orbit card. If colour is used, the logo should be in its standard colours (as provided for the K9 Orbit logo).

*Back of the card*
Include a smaller K9 Orbit logo on the back.

We need the following details for K9 Orbit personnel (as a template for entry):
- Name
- Company Position
- Mobile Number
- Email
- Office Address
- Include the K9 Orbit website: www.k9orbit.com.au

Overall, we'd like to see a design that communicates the adventure of space, professional integrity, and customer service. We look forward to seeing what you can come up with.

Target Market(s)

We provide high quality professional services for the Australian space industry. Our clients include the Southern Stellar Bureau and companies working in the space industry.

Contact Information for Business Card

- Name
- Company Position
- Mobile Number
- Email
- Office Address

Requirements
Must have
• See project description.

```html
<!DOCTYPE html>
<html lang="en">
<head>
<meta charset="utf-8">
<title>K9 Orbit – Business Card</title>
<link rel="stylesheet" href="https://fonts.googleapis.com/css2?family=Montserrat:wght@500;600;700&family=Roboto:wght@400&display=swap">
<style>
  :root {
    --backdrop: #2b2b2d;
    --navy: #2a2a77;
    --navy-light: #34348a;
    --white: #ffffff;
    --blue: #1b75c0;
    --grey-text: #6d6e71;
    --grey-line: #8a8a8f;
  }
  * { box-sizing: border-box; margin: 0; padding: 0; }
  html, body { width: 1200px; height: 881px; overflow: hidden; }
  body {
    background: var(--backdrop);
    position: relative;
    font-family: "Roboto", Arial, sans-serif;
  }
  .card {
    position: absolute;
    width: 540px;
    height: 310px;
    border-radius: 18px;
    overflow: hidden;
    box-shadow: 0 14px 30px rgba(0,0,0,0.45);
  }
  /* Front */
  .card--front {
    left: 90px; top: 80px;
    background: linear-gradient(120deg, var(--navy-light) 0%, var(--navy) 45%, var(--navy) 100%);
    display: flex; align-items: center; justify-content: center;
  }
  .front-brand {
    display: flex; align-items: center; gap: 18px;
    font-family: "Montserrat", Arial, sans-serif;
    font-weight: 700;
    font-size: 58px;
    letter-spacing: 4px;
    color: var(--white);
  }
  .front-brand__dot {
    width: 22px; height: 22px; border-radius: 50%;
    background: var(--white);
  }
  /* Back */
  .card--back {
    left: 570px; top: 480px;
    background: var(--white);
  }
  .back-wave { position: absolute; left: 0; bottom: 0; width: 540px; height: 130px; }
  .company {
    position: absolute; left: 30px; top: 104px;
  }
  .company__name {
    font-family: "Montserrat", Arial, sans-serif;
    font-weight: 500;
    font-size: 40px;
    line-height: 1.1;
    color: var(--grey-text);
    display: flex; align-items: center; gap: 10px;
  }
  .company__mark {
    width: 18px; height: 18px; border-radius: 50%; background: var(--blue);
  }
  .company__tagline {
    margin-top: 6px; margin-left: 28px;
    font-family: "Montserrat", Arial, sans-serif;
    font-size: 9.5px; color: var(--blue);
    letter-spacing: 0.2px;
    white-space: nowrap;
  }
  .divider {
    position: absolute; left: 300px; top: 52px;
    width: 1.5px; height: 124px; background: var(--blue);
  }
  .contact {
    position: absolute; left: 316px; top: 42px;
    color: var(--grey-text); font-size: 11.5px; line-height: 1.4;
  }
  .contact__name {
    font-family: "Montserrat", Arial, sans-serif;
    font-weight: 700; font-size: 22px; color: var(--blue);
    letter-spacing: 1px; line-height: 1.1;
  }
  .contact__role { font-size: 13px; margin-bottom: 8px; }
  .contact__address { margin-bottom: 8px; }
  .contact__row { display: flex; align-items: center; gap: 6px; }
  .contact__row svg { width: 10px; height: 10px; flex: none; }
</style>
</head>
<body>

<section class="card card--front" aria-label="Card front">
  <div class="front-brand">
    <span class="front-brand__dot"></span>
    <span>K9 Orbit</span>
  </div>
</section>

<section class="card card--back" aria-label="Card back">
  <div class="company">
    <div class="company__name"><span class="company__mark"></span>K9 Orbit</div>
    <div class="company__tagline">Labour Hire • Consultancy • Project Delivery</div>
  </div>

  <div class="divider"></div>

  <div class="contact">
    <div class="contact__name">DANIEL HARPER</div>
    <div class="contact__role">Director</div>
    <div class="contact__address">Level 2, 58/17 Harbour St<br>Westbridge VIC 3120</div>
    <div class="contact__row">
      <svg viewBox="0 0 10 10"><path d="M2 1 L4 1 L4.6 3 L3.4 4 Q4.5 6 6 6.6 L7 5.4 L9 6 L9 8 Q5 9 2 6 Q1 4 2 1 Z" fill="#1b75c0"/></svg>
      <span>+330 5172-6043</span>
    </div>
    <div class="contact__row">
      <svg viewBox="0 0 10 10"><rect x="0.5" y="2" width="9" height="6" fill="#1b75c0"/><path d="M0.5 2 L5 5.5 L9.5 2" stroke="#fff" stroke-width="0.8" fill="none"/></svg>
      <span>contact@k9orbit.com.au</span>
    </div>
    <div class="contact__row">
      <svg viewBox="0 0 10 10"><circle cx="5" cy="5" r="4.2" fill="none" stroke="#1b75c0" stroke-width="0.9"/><ellipse cx="5" cy="5" rx="1.8" ry="4.2" fill="none" stroke="#1b75c0" stroke-width="0.8"/><path d="M0.8 5 H9.2 M1.5 3 H8.5 M1.5 7 H8.5" stroke="#1b75c0" stroke-width="0.7"/></svg>
      <span>www.k9orbit.com.au</span>
    </div>
  </div>

  <svg class="back-wave" viewBox="0 0 540 130" preserveAspectRatio="none">
    <path d="M150 118 Q380 80 540 14 L540 20 Q380 88 150 118 Z" fill="#8a8a8f"/>
    <path d="M0 108 Q300 112 540 26 L540 130 L0 130 Z" fill="#1b75c0"/>
  </svg>
</section>

</body>
</html>
```